Customer flyer

Hi there,

We need a flyer done for our father's business. It is called Tidal crest and the flyer will be distributed to realtors in British Columbia. He lends money to realtors when they have sold a home from the time subjects are removed from the transaction to when the sale closes. He is looking for a modern, classy look with the following information:

"Tidal Crest"

Realtor Pay Day upon Subject Removal

Did you know?

* Fees 100% tax deductable
* Same Day Service
* Confidential
* Low Rates

Your money from 738519 B.C. Ltd. and It can be directly deposited into your bank account or delivered to your office

For quote: call Gavin Merrow 250 555 0137

This is a small business so he doesn't have a logo and has never needed to do promotions before as it's run on word of mouth for the past 10 years. We are open to all ideas and suggestions - he is a finance guy so looking to you for the creative side :)

Thank you!

I don't like the phrase Realtor Pay Day upon subject removal. I think I prefer "Realtors! Celebrate Your Home sales upon subject removal" . Your thoughts?

Thank you

```html
<!DOCTYPE html>
<html lang="en">
<head>
<meta charset="utf-8">
<title>Tidal Crest – Realtor Flyer</title>
<link href="https://fonts.googleapis.com/css2?family=Roboto+Condensed:wght@700&family=Open+Sans:wght@400;600&display=swap" rel="stylesheet">
<style>
  :root {
    --page-bg: #e9e9e9;
    --sky-light: #9cc8ec;
    --sky-mid: #3f86c8;
    --sky-deep: #123a6b;
    --desk-dark: #0d2440;
    --band-blue: #3f87c8;
    --band-edge: #1d4f82;
    --title-yellow: #e9e81e;
    --accent-yellow: #f2ef1a;
    --panel-black: #000000;
    --paper: #f4f5f7;
    --paper-shade: #d9dce1;
    --white: #ffffff;
  }
  * { box-sizing: border-box; margin: 0; padding: 0; }
  html, body {
    width: 1200px; height: 900px; overflow: hidden;
    background: var(--page-bg);
  }
  .flyer {
    position: absolute; left: 305px; top: 35px;
    width: 590px; height: 830px;
    background: linear-gradient(180deg, var(--paper) 60%, var(--paper-shade));
    box-shadow: 0 6px 18px rgba(0,0,0,.25);
    overflow: hidden;
  }
  .hero-photo {
    position: absolute; left: 0; top: 0; width: 590px; height: 482px;
    background:
      linear-gradient(180deg, transparent 62%, var(--desk-dark) 100%),
      linear-gradient(160deg, var(--sky-deep) 0%, var(--sky-mid) 35%, var(--sky-light) 55%, var(--sky-mid) 75%, var(--sky-deep) 100%);
  }
  .brand-title {
    position: absolute; left: 0; width: 100%; top: 418px;
    text-align: center;
    font-family: "Roboto Condensed", "Arial Narrow", sans-serif;
    font-weight: 700; font-size: 54px; letter-spacing: 0.5px;
    color: var(--title-yellow);
  }
  .headline-band {
    position: absolute; left: 4px; top: 482px; width: 582px; height: 70px;
    background: var(--band-blue);
    clip-path: polygon(7% 0, 93% 0, 100% 100%, 0 100%);
    text-align: center; color: var(--white);
    font-family: "Roboto Condensed", "Arial Narrow", sans-serif; font-weight: 700;
  }
  .headline-band .shout { font-size: 27px; line-height: 32px; padding-top: 6px; }
  .headline-band .pitch { font-size: 20px; line-height: 26px; }
  .info-panel {
    position: absolute; top: 552px; height: 198px;
    background: var(--panel-black); color: var(--white);
    font-family: "Open Sans", Arial, sans-serif;
    box-shadow: 0 3px 8px rgba(0,0,0,.45);
  }
  .facts-panel { left: 35px; width: 253px; padding: 22px 0 0 26px; }
  .deposit-panel { left: 308px; width: 254px; padding: 18px 0 0 16px; }
  .facts-panel h2 {
    font-size: 21px; font-weight: 400; color: var(--accent-yellow);
    margin: 0 0 12px 8px;
  }
  .fact-list { list-style: none; }
  .fact-list li {
    font-size: 17px; line-height: 30px; position: relative; padding-left: 16px;
  }
  .fact-list li::before {
    content: ""; position: absolute; left: 0; top: 11px;
    width: 8px; height: 8px; background: var(--accent-yellow);
  }
  .deposit-panel p { font-size: 17px; line-height: 31.5px; }
  .deposit-panel .hl { color: var(--accent-yellow); }
  .call-bar {
    position: absolute; left: 0; top: 766px; width: 590px; height: 56px;
    background: linear-gradient(180deg, var(--band-blue), var(--band-edge));
    color: var(--white); text-align: center;
    font-family: "Roboto Condensed", "Arial Narrow", sans-serif;
    font-weight: 700; font-size: 33px; line-height: 56px;
  }
</style>
</head>
<body>
  <main class="flyer">
    <div class="hero-photo" role="img" aria-label="Blue city skyscrapers with a hand signing a contract on a desk"></div>
    <h1 class="brand-title">TIDAL CREST</h1>

    <header class="headline-band">
      <div class="shout">REALTORS!</div>
      <div class="pitch">CELEBRATE YOUR HOME SALES UPON SUBJECT REMOVAL</div>
    </header>

    <section class="info-panel facts-panel">
      <h2>Did you know?</h2>
      <ul class="fact-list">
        <li>Fees 100% tax deductable</li>
        <li>Same Day Service</li>
        <li>Confidential</li>
        <li>Low Rates</li>
      </ul>
    </section>

    <section class="info-panel deposit-panel">
      <p>Your money from <span class="hl">738519 B.C. Ltd.</span> and It can be directly <span class="hl">deposited</span> into your <span class="hl">bank account</span> or delivered to your office</p>
    </section>

    <footer class="call-bar">Call Gavin Merrow 250 555 0137</footer>
  </main>
</body>
</html>
```